I work in creative/artistic projects across different mediums.
It needs to communicate creativity, style, sexy, uniqueness, individuality and sophistication.
It should not look corporate.
Colours I like are black silver gold deep purple, chocolate, orchid.
It doesn't have to make use of all these colours.
I do not like bright primary colors.
Updates

Project Deadline Extended
Reason: Still in the communication process and to allow the person enough time to finish the design. Though i should know in the next day or two. Thank you.

Target Market(s)

creatives and companies wanting to inject creativity into thier business.

Industry/Entity Type

Work

Contact Information for Business Card

Lionel Crowthwick
0418359026
lionel@lionelcrowthwick.com

quietsilverhour.com.au

Requirements
Should not have
• Anything corporate OR OLD FASHIONED

```html
<!DOCTYPE html>
<html lang="en">
<head>
<meta charset="utf-8">
<title>Lionel Crowthwick — Business Card</title>
<link rel="stylesheet" href="https://fonts.googleapis.com/css2?family=Oswald:wght@300;400&family=Josefin+Sans:wght@400;600&display=swap">
<style>
  :root {
    --page-bg: #f1f0ed;
    --card-deep: #1f2a1d;
    --card-mid: #3a4636;
    --card-edge: #141b13;
    --gold: #e9cf6a;
    --gold-soft: #c9a840;
    --shadow: rgba(0, 0, 0, 0.28);
  }

  * { margin: 0; padding: 0; box-sizing: border-box; }

  html, body {
    width: 1200px;
    height: 700px;
    overflow: hidden;
    background: var(--page-bg);
  }

  .canvas {
    position: relative;
    width: 1200px;
    height: 700px;
    display: flex;
    align-items: center;
    justify-content: center;
  }

  .business-card {
    position: relative;
    width: 720px;
    height: 440px;
    border-radius: 4px;
    overflow: hidden;
    box-shadow: 0 18px 40px var(--shadow);
  }

  .damask-backdrop {
    position: absolute;
    inset: 0;
    background:
      radial-gradient(ellipse at 50% 40%, var(--card-mid) 0%, var(--card-deep) 60%, var(--card-edge) 100%);
  }

  .card-content {
    position: absolute;
    inset: 0;
    display: flex;
    flex-direction: column;
    align-items: center;
    padding-top: 92px;
    color: var(--gold);
  }

  .name-rule {
    display: block;
    width: 210px;
    height: 14px;
  }

  .holder-name {
    font-family: "Oswald", sans-serif;
    font-weight: 300;
    font-size: 44px;
    letter-spacing: 2px;
    text-transform: uppercase;
    line-height: 1;
    margin: 8px 0 6px;
    color: var(--gold);
  }

  .contact-list {
    list-style: none;
    margin-top: 28px;
    font-family: "Josefin Sans", sans-serif;
    font-weight: 400;
    font-size: 19px;
    letter-spacing: 1.5px;
    text-transform: uppercase;
    line-height: 1.55;
    text-align: left;
  }

  .contact-phone {
    padding-left: 110px;
  }

  .closing-rule {
    width: 34px;
    height: 2px;
    margin-top: 26px;
    background: var(--gold-soft);
  }
</style>
</head>
<body>
  <main class="canvas">
    <article class="business-card">
      <div class="damask-backdrop" role="img" aria-label="Dark green damask pattern of trailing floral vines covering the card"></div>

      <div class="card-content">
        <svg class="name-rule" viewBox="0 0 210 14" aria-hidden="true">
          <line x1="10" y1="7" x2="200" y2="7" stroke="#e9cf6a" stroke-width="1.5"/>
          <line x1="80" y1="10" x2="130" y2="10" stroke="#e9cf6a" stroke-width="1"/>
        </svg>

        <h1 class="holder-name">Lionel Crowthwick</h1>

        <svg class="name-rule" viewBox="0 0 210 14" aria-hidden="true">
          <line x1="80" y1="4" x2="130" y2="4" stroke="#e9cf6a" stroke-width="1"/>
          <line x1="10" y1="7" x2="200" y2="7" stroke="#e9cf6a" stroke-width="1.5"/>
        </svg>

        <ul class="contact-list">
          <li class="contact-phone">0418359026</li>
          <li class="contact-email">lionel@lionelcrowthwick.com</li>
          <li class="contact-web">www.quietsilverhour.com.au</li>
        </ul>

        <span class="closing-rule" aria-hidden="true"></span>
      </div>
    </article>
  </main>
</body>
</html>
```